Packaging for Hair Fibers Product

We are a start up company looking for a new packaging design for hair building fibers. These are aimed at predominantly men but also women as well. We already have a logo and i have the packaging design from our competitors. We are wanting to keep the look masculine as 90% of our users will be middle aged men. We would like the colours to be black and white but are open to other colours as well.
It will need to have our logo and the following somewhere on the front.
"Instant Fuller & Thicker Hair" & "Natural Hair Building Fibers" "28g" or "Net Weight 28g"
We only need the front of the packaging designed, please make the other sides of the packaging the same colour but blank.
Target Market(s)
Men 25+
Industry/Entity Type
Hair And Beauty
Requirements
Must have
- Logo which i have included. and the following somewhere on the front.
- "Instant Fuller & Thicker Hair" ; "Natural Hair Building Fibers" "28g" or "Net Weight 28g"
Nice to have
- Make it stand out from the competition or similar to the brantiq example.

```html
<!DOCTYPE html>
<html lang="en">
<head>
<meta charset="utf-8">
<title>Corvane Hair Building Fibers – Box Front</title>
<link rel="stylesheet" href="https://fonts.googleapis.com/css2?family=Josefin+Sans:wght@300&family=Open+Sans:wght@400&family=Marcellus&display=swap">
<style>
  :root {
    --page: #ffffff;
    --box: #262624;
    --box-edge: #1a1a19;
    --gold: #f3d9a0;
    --grey: #a3a3a3;
  }
  html, body {
    margin: 0;
    padding: 0;
    width: 829px;
    height: 1200px;
    overflow: hidden;
    background: var(--page);
  }
  .canvas {
    position: relative;
    width: 829px;
    height: 1200px;
  }
  .box-front {
    position: absolute;
    left: 214px;
    top: 232px;
    width: 398px;
    height: 727px;
    background: var(--box);
    border-top: 2px solid var(--box-edge);
  }
  .brand-name,
  .tagline {
    position: absolute;
    writing-mode: vertical-rl;
    transform: rotate(180deg);
    white-space: nowrap;
    color: var(--gold);
    margin: 0;
  }
  .brand-name {
    left: 72px;
    bottom: 147px;
    font-family: "Josefin Sans", sans-serif;
    font-weight: 300;
    font-size: 58px;
    letter-spacing: 6px;
    line-height: 1;
  }
  .tagline {
    left: 155px;
    bottom: 147px;
    font-family: "Open Sans", sans-serif;
    font-size: 18px;
    letter-spacing: 0.3px;
    line-height: 1;
  }
  .fibers-line {
    position: absolute;
    left: 0;
    right: 0;
    top: 596px;
    margin: 0;
    text-align: center;
    font-family: "Marcellus", serif;
    font-size: 18px;
    color: var(--grey);
  }
  .net-weight {
    position: absolute;
    left: 0;
    right: 0;
    top: 663px;
    margin: 0;
    text-align: center;
    font-family: "Open Sans", sans-serif;
    font-size: 17px;
    color: var(--gold);
  }
</style>
</head>
<body>
  <main class="canvas">
    <section class="box-front" aria-label="Hair building fibers box, front panel">
      <h1 class="brand-name">CORVANE</h1>
      <p class="tagline">INSTANT FULLER &amp; THICKER HAIR</p>
      <p class="fibers-line">Natural Hair Building Fibers</p>
      <p class="net-weight">Net Weight 28g</p>
    </section>
  </main>
</body>
</html>
```